Gardener needs an exciting new flyer design.

I'm a passionate gardener that requires a custom flyer design for a owner operator gardening business. Design will be for a DL flyer. I'm based on the Sunshine coast in Queensland Australia. My target audience is the residential market on the Sunshine coast. Business name is Marlowe Greens. My services are, lawn mowing, weeding, Eco Friendly fertilizing, green waste removal, Mulching, tree and shrub pruning, Full garden makeovers, hedging, pressure cleaning, privacy screening, Timber deck rejuvenation, Planting, Turf preparation and installation, and much more. Free no obligation quotes, reliable and friendly service, great rates. 12 years experience. Web www.marlowegreens.com.au - Phone 0418527064 - Email doug@marlowegreens.com.au I would like the design to portray a friendly and professional approach.

Target Market(s)

Residential

Industry/Entity Type

Gardener

Font styles to use
Serif

Colors
9ccb3b
abd037
3176b5

Requirements
Must have
• my services, my logo, my contact details,

```html
<!DOCTYPE html>
<html lang="en">
<head>
<meta charset="utf-8">
<title>Marlowe Greens – DL Flyer</title>
<link href="https://fonts.googleapis.com/css2?family=Lato:ital,wght@0,300;0,400;0,700;1,300;1,400&display=swap" rel="stylesheet">
<style>
:root{
  --green:#3b8f3e;
  --green-dark:#2f7a33;
  --paper:#efefe9;
  --ink:#333333;
  --ink-soft:#555555;
  --stage:#dcdcdf;
  --white:#ffffff;
}
*{box-sizing:border-box;margin:0;padding:0}
html,body{width:1200px;height:1200px;overflow:hidden}
body{background:var(--stage);font-family:'Lato',sans-serif;color:var(--ink);position:relative}

.flyer{position:absolute;top:100px;width:480px;height:1000px;background:var(--paper);overflow:hidden;box-shadow:0 6px 18px rgba(0,0,0,.18)}
.flyer--front{left:80px}
.flyer--back{left:640px}

/* front */
.brand{position:absolute;left:30px;top:24px;width:220px;display:flex;flex-direction:column;align-items:center;gap:8px}
.brand__dot{width:46px;height:46px;border-radius:50%;background:var(--green)}
.brand__name{font-weight:700;font-size:26px;line-height:30px;color:var(--green);white-space:nowrap}
.contact{position:absolute;right:24px;top:30px;font-size:12px;line-height:18px;color:var(--ink)}
.contact li{list-style:none;display:flex;align-items:center;gap:6px;justify-content:flex-end;white-space:nowrap}
.contact svg{width:11px;height:11px;flex:none}

.hero{position:absolute;left:-20px;top:150px;width:520px;height:440px;background:var(--green);border-radius:50% 50% 50% 50% / 22% 22% 28% 28%;overflow:hidden}
.hero__photo{position:absolute;left:0;top:0;width:520px;height:425px;border-radius:50% 50% 50% 50% / 22% 22% 28% 28%;
  background:linear-gradient(180deg,#8fb5d6 0%,#b7cbd6 22%,#e7e4de 34%,#b9b7ad 44%,#6da63a 56%,#4f8f27 100%)}
.bubble{position:absolute;border-radius:50%;border:7px solid var(--green)}
.bubble--mower{left:330px;top:110px;width:180px;height:180px;background:radial-gradient(circle at 50% 45%,#7f94a8,#6b9a3c 70%)}
.bubble--mulch{left:255px;top:160px;width:115px;height:115px;background:radial-gradient(circle at 50% 55%,#8a5a35,#5a7a34 80%)}

.about{position:absolute;left:22px;top:615px;width:240px}
.about__title{font-weight:700;font-size:22px;color:var(--green);letter-spacing:-.5px;display:inline-block;border-bottom:2px solid var(--ink);padding-bottom:2px;margin-left:20px}
.about__text{margin-top:18px;font-style:italic;font-weight:300;font-size:13px;line-height:21px;text-align:justify;color:var(--ink)}
.tagline{position:absolute;left:286px;top:625px;font-weight:300;font-size:29px;line-height:38px;color:var(--ink)}
.tagline strong{font-weight:400;color:var(--green)}

.call{position:absolute;left:0;bottom:0;width:100%;height:175px;background:var(--green);color:var(--white);text-align:center}
.call__lead{margin-top:22px;font-style:italic;font-size:21px}
.call__phone{margin-top:6px;font-style:italic;font-size:44px;display:flex;justify-content:center;align-items:center;gap:10px}
.call__phone svg{width:34px;height:34px}
.call__area{margin-top:8px;font-style:italic;font-size:15px}

/* back */
.banner{position:absolute;left:0;top:0;width:480px;height:285px;background:var(--green);border-radius:0 0 50% 50% / 0 0 18% 18%}
.banner__photo{position:absolute;left:0;top:0;width:480px;height:270px;border-radius:0 0 50% 50% / 0 0 14% 14%;
  background:linear-gradient(180deg,#6f8a4e 0%,#93a86a 35%,#7fb040 60%,#4f8d22 100%)}
.section-title{position:absolute;width:100%;text-align:center;font-weight:700;color:var(--green);letter-spacing:-.3px}
.section-title--garden{top:320px;font-size:26px}
.section-title--other{top:640px;font-size:30px}
.thumb{position:absolute;left:30px;width:200px}
.thumb--hedge{top:360px;height:115px;background:linear-gradient(180deg,#5f8f3a,#3f7a2a 70%,#88a060)}
.thumb--venue{top:490px;height:110px;background:linear-gradient(180deg,#3f6a3a,#d9c3a8 60%,#c9a77f)}
.services{position:absolute;left:248px;top:370px;list-style:none;font-size:14.5px;line-height:25.5px;color:var(--ink)}
.tick{color:var(--green);font-weight:700;margin-right:7px}
.other{position:absolute;top:690px;width:100%;text-align:center;font-size:15px;line-height:22px;color:var(--ink)}
.perks{position:absolute;left:0;bottom:0;width:100%;height:225px;background:var(--green);color:var(--white);text-align:center;padding-top:22px;font-size:30px;line-height:42px}
.perks .tick{color:var(--white);font-size:24px}
</style>
</head>
<body>

<section class="flyer flyer--front">
  <div class="brand">
    <span class="brand__dot"></span>
    <span class="brand__name">Marlowe Greens</span>
  </div>
  <ul class="contact">
    <li><svg viewBox="0 0 12 12"><circle cx="6" cy="6" r="5" fill="none" stroke="#3b8f3e" stroke-width="1.5"/><path d="M1 6h10M6 1c-2.5 3-2.5 7 0 10M6 1c2.5 3 2.5 7 0 10" fill="none" stroke="#3b8f3e" stroke-width="1"/></svg>www.marlowegreens.com.au</li>
    <li><svg viewBox="0 0 12 12"><rect x="1" y="2.5" width="10" height="7" fill="#3b8f3e"/><path d="M1 2.5l5 4 5-4" fill="none" stroke="#fff" stroke-width="1"/></svg>doug@marlowegreens.com.au</li>
  </ul>

  <div class="hero">
    <div class="hero__photo" role="img" aria-label="Photo of a white house with a freshly mown striped lawn"></div>
  </div>
  <div class="bubble bubble--mower" role="img" aria-label="Photo of a ride-on lawn mower"></div>
  <div class="bubble bubble--mulch" role="img" aria-label="Photo of a wheelbarrow full of mulch"></div>

  <div class="about">
    <h2 class="about__title">ABOUT US</h2>
    <p class="about__text">Marlowe Greens is your garden and lawn care specialist, with a passion for gardening and a keen eye for detail you can rest assured you're in the right hands. Our services are tailored to meet every individual clients needs. looking amazing.</p>
  </div>
  <p class="tagline">A BEAUTIFUL<br><strong>GARDEN</strong><br>DOESN'T<br>HAPPEN BY<br>ITSELF!</p>

  <div class="call">
    <p class="call__lead">JUST A PHONE CALL AWAY</p>
    <p class="call__phone"><svg viewBox="0 0 24 24"><path d="M6.6 10.8a15 15 0 0 0 6.6 6.6l2.2-2.2c.3-.3.7-.4 1-.2 1.1.4 2.3.6 3.6.6.6 0 1 .4 1 1V20c0 .6-.4 1-1 1A17 17 0 0 1 3 4c0-.6.4-1 1-1h3.5c.6 0 1 .4 1 1 0 1.3.2 2.5.6 3.6.1.3 0 .7-.2 1z" fill="#fff"/><path d="M15 3a6 6 0 0 1 6 6M15 6a3 3 0 0 1 3 3" fill="none" stroke="#fff" stroke-width="1.6"/></svg>0418527064</p>
    <p class="call__area">Servicing Noosa to Caloundra and everywhere in-between.</p>
  </div>
</section>

<section class="flyer flyer--back">
  <div class="banner">
    <div class="banner__photo" role="img" aria-label="Photo of a lawn mower being pushed across green grass"></div>
  </div>

  <h2 class="section-title section-title--garden">GARDEN SERVICES</h2>
  <div class="thumb thumb--hedge" role="img" aria-label="Photo of neatly trimmed garden hedges"></div>
  <div class="thumb thumb--venue" role="img" aria-label="Photo of a garden set up for an outdoor wedding"></div>
  <ul class="services">
    <li><span class="tick">✓</span>Lawn mowing</li>
    <li><span class="tick">✓</span>Turf preparation and installation</li>
    <li><span class="tick">✓</span>Tree and shrub pruning</li>
    <li><span class="tick">✓</span>Fertilizing</li>
    <li><span class="tick">✓</span>Full garden makeovers</li>
    <li><span class="tick">✓</span>Green waste removal</li>
    <li><span class="tick">✓</span>Garden mulching</li>
    <li><span class="tick">✓</span>Hedging</li>
    <li><span class="tick">✓</span>Weeding</li>
  </ul>

  <h2 class="section-title section-title--other">OTHER SERVICES</h2>
  <div class="other">
    <p><span class="tick">✓</span>Aluminium fencing and gate installation and repairs</p>
    <p><span class="tick">✓</span>Timber decking rejuvenation and repairs</p>
    <p><span class="tick">✓</span>Pressure cleaning &nbsp;&nbsp;<span class="tick">✓</span>And much more!</p>
  </div>

  <div class="perks">
    <p><span class="tick">✓</span>Free no obligation quotes</p>
    <p><span class="tick">✓</span>Reliable and friendly service</p>
    <p><span class="tick">✓</span>Great rates</p>
    <p><span class="tick">✓</span>12 years experience</p>
  </div>
</section>

</body>
</html>
```